Book Cover Design Project - Lesbian stories

I need a cover for my ebook of short stories. Target market is lesbians. I want something erotic (but not too over the top or porny). Something tasteful and feminine. For example two women with a flower see artist Mirel Dunstan http://www.galvoristudio.example/magazine/article.php?articleID=287.

Title: Harbour Letters, Paper Moons

By Lucinda Marvaro

```html
<!DOCTYPE html>
<html lang="en">
<head>
<meta charset="utf-8">
<title>Harbour Letters, Paper Moons — Cover Spread</title>
<link rel="stylesheet" href="https://fonts.googleapis.com/css2?family=Sniglet:wght@400;800&family=Comfortaa:wght@400;600&family=Open+Sans:wght@700;800&display=swap">
<style>
  :root {
    --stage: #ececec;
    --cover-pink: #f3aad2;
    --back-pink: #d975a8;
    --spine-magenta: #c8177c;
    --ornament-magenta: #d2338f;
    --title-fill: #ea2a86;
    --title-soft: #f9cfe4;
    --title-line: #5b0b30;
    --ink: #3a1025;
    --box-grey: #d6d6d6;
    --box-ink: #222;
    --art-blush: #f8c6df;
    --art-rose: #f07fb5;
    --art-red: #e23a73;
    --art-violet: #7b3fa6;
    --art-sky: #3fb4e6;
    --art-sun: #f2e23a;
  }
  * { box-sizing: border-box; margin: 0; padding: 0; }
  html, body { width: 1200px; height: 800px; overflow: hidden; }
  body { background: var(--stage); position: relative; font-family: "Open Sans", Arial, sans-serif; }

  .spread {
    position: absolute; left: 186px; top: 110px;
    width: 828px; height: 580px;
    display: flex;
    box-shadow: 0 14px 30px rgba(0,0,0,.18);
  }

  /* Shared title */
  .title-block { position: absolute; text-align: center; color: var(--title-fill); line-height: 1; }
  .title-block .author { display: block; font-weight: 700; color: var(--ink); text-align: right; }
  .title-block .line-bold {
    display: block; font-family: "Sniglet", sans-serif; font-weight: 800;
    text-transform: uppercase;
    -webkit-text-stroke: 1.5px var(--title-line); paint-order: stroke fill;
  }
  .title-block .line-light {
    display: block; font-family: "Comfortaa", sans-serif; font-weight: 600;
    text-transform: uppercase; color: var(--title-soft);
    -webkit-text-stroke: 0.8px var(--title-line); paint-order: stroke fill;
  }

  /* Back cover */
  .back-cover {
    position: relative; width: 400px; height: 580px;
    background: var(--back-pink); overflow: hidden;
  }
  .back-cover .ornament-strip {
    position: absolute; left: 0; top: 0; width: 46px; height: 100%;
    background: linear-gradient(180deg, var(--ornament-magenta), #b81a72 60%, var(--ornament-magenta));
  }
  .back-cover .title-block { left: 70px; right: 40px; top: 22px; }
  .back-cover .title-block .author { font-size: 10px; padding-right: 58px; margin-bottom: 3px; }
  .back-cover .title-block .line-bold { font-size: 32px; }
  .back-cover .title-block .line-light { font-size: 24px; }
  .blurb {
    position: absolute; left: 56px; right: 26px; top: 174px;
    font-size: 11.2px; line-height: 1.55; font-weight: 700;
    color: var(--ink); text-align: justify;
  }
  .back-boxes { position: absolute; left: 62px; right: 32px; bottom: 28px; display: flex; justify-content: space-between; }
  .back-boxes .placeholder-box {
    width: 128px; height: 46px; background: var(--box-grey);
    display: flex; align-items: center; justify-content: center;
    font-weight: 800; font-size: 14px; color: var(--box-ink);
  }

  /* Spine */
  .spine {
    width: 28px; height: 580px; background: var(--spine-magenta);
    display: flex; align-items: center; justify-content: space-between;
    writing-mode: vertical-rl; padding: 18px 0;
    color: #fbd6ea;
  }
  .spine .spine-title { font-family: "Sniglet", sans-serif; font-weight: 800; font-size: 15px; letter-spacing: 1px; text-transform: uppercase; }
  .spine .spine-author { font-size: 10px; font-weight: 700; }

  /* Front cover */
  .front-cover {
    position: relative; width: 400px; height: 580px;
    background: var(--cover-pink); overflow: hidden;
  }
  .front-cover .illustration {
    position: absolute; left: 30px; top: 196px; width: 324px; height: 384px;
  }
  .front-cover .ornament-left {
    position: absolute; left: 0; top: 0; width: 30px; height: 200px;
    background: linear-gradient(180deg, var(--ornament-magenta), rgba(210,51,143,0));
  }
  .front-cover .ornament-right {
    position: absolute; right: 0; top: 0; width: 46px; height: 100%;
    background: linear-gradient(180deg, var(--ornament-magenta), #e04a9c 50%, var(--ornament-magenta));
  }
  .front-cover .ornament-corner {
    position: absolute; left: 0; bottom: 0; width: 110px; height: 130px;
    background: radial-gradient(circle at 0 100%, #c01f78 0 55%, rgba(192,31,120,0) 75%);
  }
  .front-cover .title-block { left: 44px; right: 50px; top: 30px; }
  .front-cover .title-block .author { font-size: 12px; padding-right: 30px; margin-bottom: 4px; }
  .front-cover .title-block .line-bold { font-size: 42px; }
  .front-cover .title-block .line-light { font-size: 30px; }
</style>
</head>
<body>
  <main class="spread">
    <section class="back-cover">
      <div class="ornament-strip" role="img" aria-label="Magenta floral vine ornament"></div>
      <h2 class="title-block">
        <span class="author">Lucinda Marvaro’s</span>
        <span class="line-bold">Harbour</span>
        <span class="line-light">Letters</span>
        <span class="line-bold">Paper</span>
        <span class="line-light">Moons</span>
      </h2>
      <p class="blurb">Lorem ipsum dolor sit amet, consectetur adipisicing elit, sed do eiusmod tempor incididunt ut labore et dolore magna aliqua. Ut enim ad minim veniam, quis nostrud exercitation. Lorem ipsum dolor sit amet, consectetur adipisicing elit, sed do eiusmod tempor incididunt ut labore et dolore magna aliqua. Ut enim ad minim veniam, quis nostrud exercitation. Lorem ipsum dolor sit amet, consectetur adipisicing elit, sed do eiusmod tempor incididunt ut labore et dolore magna aliqua. Ut enim ad minim veniam, quis nostrud exercitation. Lorem ipsum dolor sit amet, consectetur adipisicing elit, sed do eiusmod tempor incididunt ut labore et dolore magna aliqua. Ut enim ad minim veniam, quis nostrud exercitation. Lorem ipsum dolor sit amet, consectetur adipisicing elit, sed do eiusmod tempor incididunt ut labore et dolore magna aliqua. Ut enim ad minim veniam, quis nostrud exercitation. Lorem</p>
      <div class="back-boxes">
        <div class="placeholder-box">LOGO</div>
        <div class="placeholder-box">ISBN</div>
      </div>
    </section>

    <aside class="spine">
      <span class="spine-title">Harbour Letters, Paper Moons</span>
      <span class="spine-author">Lucinda Marvaro</span>
    </aside>

    <section class="front-cover">
      <svg class="illustration" viewBox="0 0 324 384" preserveAspectRatio="none" role="img" aria-label="Illustration of two fashionable women, one in a blue top and purple trousers, one in a yellow dress, facing each other in front of a large pink heart">
        <defs>
          <linearGradient id="art-tones" x1="0" y1="0" x2="1" y2="1">
            <stop offset="0" stop-color="var(--art-blush)"/>
            <stop offset="0.3" stop-color="var(--art-rose)"/>
            <stop offset="0.55" stop-color="var(--art-red)"/>
            <stop offset="0.8" stop-color="var(--art-rose)"/>
            <stop offset="1" stop-color="var(--art-blush)"/>
          </linearGradient>
        </defs>
        <rect width="324" height="384" rx="14" fill="url(#art-tones)"/>
      </svg>
      <div class="ornament-left" role="img" aria-label="Magenta floral vine ornament"></div>
      <div class="ornament-right" role="img" aria-label="Magenta floral vine ornament"></div>
      <div class="ornament-corner" role="img" aria-label="Cluster of magenta flowers"></div>
      <h1 class="title-block">
        <span class="author">Lucinda Marvaro’s</span>
        <span class="line-bold">Harbour</span>
        <span class="line-light">Letters</span>
        <span class="line-bold">Paper</span>
        <span class="line-light">Moons</span>
      </h1>
    </section>
  </main>
</body>
</html>
```